We need a business card design for a new brand within our existing financial marketing business. Our new brand is www.qalvenport.co.uk

We attach various logo files - please use the version that will produce the sharpest image on the business card.

We are flexible about shape of card etc. Please think outside the box as to what goes on front and what goes on back of the card.

The card needs to be corporate, but really catch the eye ( e.g. premium translucent cards on plastic etc or metal cards or shiny surface etc )

We want to be able to amend the card (once the design has been agreed ) to add additional staff details, but the text to go on it will be generic

Details to go on card ( for the first generic one) are fairly minimal as we don't like cluttered business cards:-

Owen Tagget
Managing Director

Mobile: 07852 418 207
Email: o.tagget@qalvenport.co.uk

Financial

```html
<!DOCTYPE html>
<html lang="en">
<head>
<meta charset="utf-8">
<title>Qalvenport business card</title>
<link href="https://fonts.googleapis.com/css2?family=Open+Sans:ital,wght@0,400;0,600;1,700&display=swap" rel="stylesheet">
<style>
  :root {
    --backdrop: #e4e4e2;
    --card: #ffffff;
    --brand-blue: #0f74bc;
    --brand-gold: #e0aa2a;
    --ink: #3b3b3b;
    --ink-soft: #5a5a5a;
    --rule: #8fb6d9;
  }
  * { box-sizing: border-box; margin: 0; padding: 0; }
  html, body {
    width: 1200px;
    height: 899px;
    overflow: hidden;
    background: var(--backdrop);
    font-family: "Open Sans", Arial, sans-serif;
  }
  .sheet {
    position: relative;
    width: 1200px;
    height: 899px;
  }
  .card {
    position: absolute;
    top: 300px;
    width: 520px;
    height: 300px;
    background: var(--card);
    border-radius: 34px;
    overflow: hidden;
    box-shadow: 0 6px 18px rgba(0,0,0,0.12);
  }
  .card--front { left: 50px; }
  .card--back { left: 630px; }

  .brand-name {
    position: absolute;
    font-weight: 400;
    font-size: 30px;
    color: var(--brand-blue);
    line-height: 1;
  }
  .card--front .brand-name { left: 34px; top: 68px; }
  .card--back .brand-name {
    left: 50%;
    top: 50%;
    transform: translate(-50%, -50%);
    font-size: 42px;
  }

  .divider {
    position: absolute;
    left: 284px;
    top: 34px;
    width: 1px;
    height: 140px;
    background: var(--rule);
  }
  .contact {
    position: absolute;
    left: 300px;
    top: 34px;
    color: var(--ink-soft);
    font-size: 12.5px;
    line-height: 1.45;
  }
  .contact__name {
    font-weight: 700;
    font-style: italic;
    color: var(--brand-blue);
    font-size: 16px;
    line-height: 1.2;
  }
  .contact__role {
    color: var(--ink);
    font-size: 14px;
    margin-bottom: 10px;
  }
  .contact__address { margin-bottom: 4px; }
  .contact__line {
    display: flex;
    align-items: center;
    gap: 6px;
  }
  .contact__line svg { width: 11px; height: 11px; fill: var(--brand-blue); flex: none; }
  .contact__web { margin-top: 2px; }

  .footer-band {
    position: absolute;
    left: 0;
    right: 0;
    bottom: 0;
    height: 70px;
    background: var(--brand-blue);
    border-top: 4px solid var(--brand-gold);
  }
</style>
</head>
<body>
<main class="sheet">
  <section class="card card--front" aria-label="Card front">
    <div class="brand-name">Qalvenport</div>

    <div class="divider"></div>

    <div class="contact">
      <div class="contact__name">Owen Tagget</div>
      <div class="contact__role">Managing Director</div>
      <div class="contact__address">27 Harbour Row, Level 4<br>Norwich NR1</div>
      <div class="contact__line">
        <svg viewBox="0 0 12 12"><path d="M2.5 0.8l2 2.2-1 1.3c.7 1.5 1.8 2.6 3.2 3.3l1.3-1 2.2 2-1.2 2.4C4.6 10.6 1.2 7.2 0.2 2z"/></svg>
        <span>07852 418 207</span>
      </div>
      <div class="contact__line">
        <svg viewBox="0 0 12 12"><rect x="2.5" y="0" width="7" height="12" rx="1.2"/><rect x="3.8" y="1.5" width="4.4" height="7.5" fill="#fff"/></svg>
        <span>07852 418 207</span>
      </div>
      <div class="contact__line">
        <svg viewBox="0 0 12 12"><rect x="0" y="2" width="12" height="8" rx="1"/><path d="M0.5 2.5L6 6.8 11.5 2.5" fill="none" stroke="#fff" stroke-width="1"/></svg>
        <span>o.tagget@qalvenport.co.uk</span>
      </div>
      <div class="contact__web">www.qalvenport.co.uk</div>
    </div>

    <div class="footer-band"></div>
  </section>

  <section class="card card--back" aria-label="Card back">
    <div class="brand-name">Qalvenport</div>
  </section>
</main>
</body>
</html>
```